Security Company Business Card
Iron Vale
Project: Security Company Business Card
Security Company Business Card - Security
Creative Brief
Professional
Helena Brisco
Managing Director
5182 Loxley Terrace Naples, Florida USA
hbrisco@ivxsecurity.example
Be creative, new look, simple but powerful. Would like the uploaded IVX logo on the front with Iron Vale Security upload on rear
Iron Vale Security up load on the rear, but am open to creative design other than up load.
brisco7290 brisco7290
Hello Designers: Our team is looking for designs using both black/gold and red/white uploads. We are looking for something different possible a two dimension or faded look highlighting the logo to names of employees. Please show logo on rear and other opion the wording upload "Iron Vale" -Security- on the rear of card. Would like to different styles. Its importand the names on cards are clear and stand out. You need not add a web site address we will be using only email address for cards. Regards, IVX Team

```html
<!DOCTYPE html>
<html lang="en">
<head>
<meta charset="utf-8">
<title>Iron Vale Security – Business Card</title>
<link href="https://fonts.googleapis.com/css2?family=Open+Sans:wght@400;600;700&display=swap" rel="stylesheet">
<style>
  :root {
    --bg: #2b2b2d;
    --card: #ffffff;
    --navy: #1f2c63;
    --red: #e0262b;
    --ink: #3a3a3a;
  }
  * { margin: 0; padding: 0; box-sizing: border-box; }
  html, body { width: 1200px; height: 901px; overflow: hidden; }
  body {
    background: var(--bg);
    font-family: "Open Sans", Arial, sans-serif;
    position: relative;
  }
  .card {
    position: absolute;
    width: 520px;
    height: 300px;
    background: var(--card);
    border-radius: 18px;
    box-shadow: 0 14px 30px rgba(0,0,0,.45);
    overflow: hidden;
  }
  .card--back { left: 90px; top: 130px; }
  .card--front { left: 590px; top: 460px; }

  .brand {
    position: absolute;
    left: 0; right: 0; top: 50%;
    transform: translateY(-50%);
    display: flex; align-items: center; justify-content: center; gap: 14px;
  }
  .brand__dot { width: 34px; height: 34px; border-radius: 50%; background: var(--navy); }
  .brand__name {
    font-weight: 700; font-size: 30px; color: var(--navy);
    text-transform: uppercase; letter-spacing: .5px;
  }

  .person { position: absolute; left: 30px; top: 34px; }
  .person__name { color: var(--navy); font-weight: 600; font-size: 17px; }
  .person__title { color: var(--ink); font-size: 11px; margin-top: 2px; }

  .contact { position: absolute; left: 30px; top: 150px; color: var(--ink); font-size: 12.5px; line-height: 1.4; }
  .contact__address { margin-bottom: 6px; }
  .contact__row { display: flex; align-items: center; gap: 8px; }
  .contact__row svg { width: 11px; height: 11px; fill: var(--red); }
  .contact__email { margin-top: 2px; }

  .side-brand {
    position: absolute; right: 26px; top: 50%;
    transform: translateY(-50%);
    display: flex; align-items: center; gap: 10px;
  }
  .side-brand__square { width: 16px; height: 16px; background: var(--red); }
  .side-brand__name { color: var(--navy); font-weight: 700; font-size: 20px; text-transform: uppercase; }
</style>
</head>
<body>
  <section class="card card--back" aria-label="Card back">
    <div class="brand">
      <span class="brand__dot"></span>
      <span class="brand__name">Iron Vale Security</span>
    </div>
  </section>

  <section class="card card--front" aria-label="Card front">
    <div class="person">
      <div class="person__name">Helena Brisco</div>
      <div class="person__title">Managing Director</div>
    </div>

    <div class="contact">
      <div class="contact__address">5182 Loxley Terrace<br>Naples, Florida USA</div>
      <div class="contact__row">
        <svg viewBox="0 0 12 12"><path d="M2 1h3l1 3-2 1c.6 1.3 1.7 2.4 3 3l1-2 3 1v3c0 .6-.4 1-1 1C5 11 1 7 1 2c0-.6.4-1 1-1z"/></svg>
        <span>555-014-2210</span>
      </div>
      <div class="contact__row">
        <svg viewBox="0 0 12 12"><rect x="3" y="0.5" width="6" height="11" rx="1"/><rect x="4" y="2" width="4" height="7" fill="#fff"/></svg>
        <span>555-019-3384</span>
      </div>
      <div class="contact__row">
        <svg viewBox="0 0 12 12"><rect x="1" y="4" width="10" height="6" rx="1"/><rect x="3" y="1" width="6" height="3"/></svg>
        <span>555-014-7765</span>
      </div>
      <div class="contact__email">hbrisco@ivxsecurity.example</div>
    </div>

    <div class="side-brand">
      <span class="side-brand__square"></span>
      <span class="side-brand__name">Iron Vale</span>
    </div>
  </section>
</body>
</html>
```